Market Corner Fair needs a poster design

We need a poster to promote our showcase to both potential local vendors now, and visitors to the show on the actual day. See attached files and also checkout our Chatterbook page - "Market Corner Fair" for more information. Please state that booths are 8' (don't say 8' by 8'). See attached info that we have done so far, but we need something more professional. Ensure you use the Stay Bright Buy Nearby logo. The poster should be printable on both letter (8 1/2" by 11') and ledger sizes (11" by 17"). I have attached a sample of the poster from our last event - the Dwelling Expo 2013. I want the new poster similar to this (doesn't have to be exact, this is just to give you an idea.. The grand prize this time is a trip for two! The contact info has changed too, please note it on the new poster. I am no longer with my last company (UofW, Brantmoor Campus), so don't put that on the new poster. Thank you. You can email me with any questions. marketcornerfair@mailbay.example

Target Market(s)

Vendors for booth rentals. The community to visit the show.... They need to know that someone is going to win a trip for 2. We also have food, beer and wine sampling.

Industry/Entity Type

It Company

Font styles to use
Sans Serif

Requirements
Must have
• Stay bright buy nearby logo. Location. Email. Phone numbers. "Like our Chatterbook page - "Market Corner Fair". Poster is meant to attract business vendors now and to advertise the show to the public to attend in April. Must be able to print the poster on both letter size and ledger size paper. Need it in jpg too for Chatterbook uploads
Nice to have
• If it fits would be nice to say first of its kind in North Grenville
• First annual Market Corner Fair
Should not have
• Not too wordy.... Can't be confusing. Don't really need booth size on poster. Just state that both booths and marketplace tables are available. Not too many colours. We will be putting the poster in the newspaper in black and white only!

```html
<!DOCTYPE html>
<html lang="en">
<head>
<meta charset="utf-8">
<title>First Annual Market Corner Fair</title>
<link rel="stylesheet" href="https://fonts.googleapis.com/css2?family=Montserrat:wght@800&family=Josefin+Sans:wght@600;700&display=swap">
<style>
  :root {
    --page-bg: #e7e4df;
    --paper: #ffffff;
    --green-dark: #1e6a3b;
    --green-mid: #4f9a63;
    --green-soft: #a8cfae;
    --green-pale: #e3f0e4;
    --ink: #1d1d1b;
    --prize-red: #d3263a;
  }
  * { margin: 0; padding: 0; box-sizing: border-box; }
  html, body { width: 1200px; height: 872px; overflow: hidden; }
  body {
    background: var(--page-bg);
    font-family: "Josefin Sans", Arial, sans-serif;
    color: var(--ink);
    position: relative;
  }
  .poster {
    position: absolute;
    left: 283px; top: 26px;
    width: 634px; height: 820px;
    background: var(--paper);
    overflow: hidden;
  }
  .poster-header {
    position: absolute; left: 0; top: 0; width: 634px; height: 320px;
    background: radial-gradient(ellipse at 50% 95%, var(--green-pale) 0%, #f3f8f3 45%, #ffffff 100%);
  }
  .poster-title {
    position: absolute; top: 26px; left: 0; width: 100%;
    text-align: center;
    font-family: "Montserrat", Arial, sans-serif;
    font-weight: 800;
    font-size: 52px;
    line-height: 0.98;
    color: var(--green-dark);
    letter-spacing: 0.5px;
  }
  .skyline {
    position: absolute; left: 0; top: 205px; width: 634px; height: 115px;
  }
  .info-circle {
    position: absolute; top: 268px;
    width: 122px; height: 122px; border-radius: 50%;
    background: var(--paper);
    border: 4px solid var(--green-dark);
    display: flex; flex-direction: column; align-items: center; justify-content: center;
    text-align: center; color: var(--green-dark);
  }
  .date-circle { left: 14px; }
  .venue-circle { right: 14px; }
  .date-day {
    font-family: "Montserrat", Arial, sans-serif; font-weight: 800;
    font-size: 44px; line-height: 0.9;
  }
  .date-day sup { font-size: 16px; vertical-align: 22px; }
  .date-month { font-size: 14px; font-weight: 700; margin-top: 4px; color: var(--ink); }
  .date-hours { font-size: 12px; font-weight: 700; color: var(--ink); }
  .venue-name {
    font-family: "Montserrat", Arial, sans-serif; font-weight: 800;
    font-size: 15px; line-height: 1.05;
  }
  .category-list {
    position: absolute; top: 362px; left: 0; width: 100%;
    list-style: none; text-align: center;
    font-size: 21px; font-weight: 600; line-height: 1.45;
  }
  .booking-lines {
    position: absolute; top: 548px; left: 0; width: 100%;
    text-align: center; font-size: 20px; font-weight: 700; line-height: 1.45;
  }
  .prize-badge {
    position: absolute; left: 52px; top: 640px;
    width: 128px; height: 128px; border-radius: 50%;
    border: 3px dashed var(--prize-red);
    display: flex; align-items: center; justify-content: center;
    text-align: center; color: var(--prize-red);
    font-family: "Montserrat", Arial, sans-serif; font-weight: 800;
    font-size: 17px; line-height: 1.05;
  }
  .stay-bright-mark {
    position: absolute; left: 232px; top: 652px;
    text-align: center; color: var(--green-dark);
    font-family: "Montserrat", Arial, sans-serif; font-weight: 800;
    font-size: 22px; line-height: 1;
  }
  .stay-bright-mark .mark-dot {
    display: block; width: 18px; height: 18px; border-radius: 50%;
    background: var(--green-dark); margin: 0 auto 6px;
  }
  .contact-bar {
    position: absolute; left: 0; bottom: 18px; width: 100%;
    display: flex; justify-content: center; gap: 18px;
    font-size: 12.5px; font-weight: 700;
  }
  .contact-item { display: flex; align-items: center; gap: 5px; }
  .contact-icon {
    width: 22px; height: 22px; border-radius: 50%;
    border: 2px solid var(--ink);
    display: flex; align-items: center; justify-content: center;
  }
</style>
</head>
<body>
  <main class="poster">
    <section class="poster-header">
      <h1 class="poster-title">FIRST ANNUAL<br>MARKET CORNER<br>FAIR</h1>
      <svg class="skyline" viewBox="0 0 634 115" role="img" aria-label="Green town skyline silhouette with houses and buildings">
        <defs>
          <linearGradient id="skylineFill" x1="0" y1="0" x2="0" y2="1">
            <stop offset="0" stop-color="#c3dfc6"/>
            <stop offset="1" stop-color="#8fc096"/>
          </linearGradient>
        </defs>
        <rect x="0" y="20" width="634" height="95" fill="url(#skylineFill)"/>
      </svg>
    </section>

    <div class="info-circle date-circle">
      <div class="date-day">18<sup>TH</sup></div>
      <div class="date-month">APRIL 2015</div>
      <div class="date-hours">9AM-3PM</div>
    </div>
    <div class="info-circle venue-circle">
      <div class="venue-name">EASTVALE<br>CIVIC<br>CENTRE</div>
    </div>

    <ul class="category-list">
      <li>Home Services, Sales &amp; Renovations</li>
      <li>Local Dining and Confectionaries</li>
      <li>Healthy Active Living Services</li>
      <li>Weddings – Planning/Caterers/Decor</li>
      <li>Artisans &amp; One of a Kind Creations</li>
    </ul>

    <div class="booking-lines">
      <p>8' Booths available - $250 (after April 1st - $300)</p>
      <p>6' Marketplace Tables available - $150</p>
    </div>

    <div class="prize-badge">GRAND<br>PRIZE:<br>A TRIP<br>FOR 2</div>

    <div class="stay-bright-mark">
      <span class="mark-dot"></span>
      STAY<br>BRIGHT<br>BUY<br>NEARBY
    </div>

    <footer class="contact-bar">
      <div class="contact-item">
        <span class="contact-icon"></span>
        <span>/BrightLaneEvents</span>
      </div>
      <div class="contact-item">
        <span class="contact-icon">
          <svg width="12" height="12" viewBox="0 0 24 24" aria-hidden="true"><path d="M6.6 10.8a15 15 0 0 0 6.6 6.6l2.2-2.2a1 1 0 0 1 1-.25 11.4 11.4 0 0 0 3.6.57 1 1 0 0 1 1 1V20a1 1 0 0 1-1 1A17 17 0 0 1 3 4a1 1 0 0 1 1-1h3.5a1 1 0 0 1 1 1c0 1.25.2 2.45.57 3.57a1 1 0 0 1-.25 1z" fill="#1d1d1b"/></svg>
        </span>
        <span>555-014-2290</span>
      </div>
      <div class="contact-item">
        <span class="contact-icon">
          <svg width="12" height="12" viewBox="0 0 24 24" aria-hidden="true"><rect x="2" y="5" width="20" height="14" rx="1.5" fill="none" stroke="#1d1d1b" stroke-width="2.4"/><path d="M2.5 6l9.5 7 9.5-7" fill="none" stroke="#1d1d1b" stroke-width="2.4"/></svg>
        </span>
        <span>marketcornerfair@mailbay.example</span>
      </div>
    </footer>
  </main>
</body>
</html>
```